After-School Program - End of the Year Mailing to Donors

We would like to highlight some of our accomplishments from the year and ask people to donate to our organization. We are a non-profit organization that serves underprivileged children with after school programs. We want a 6x9 flyer with printing on both sides that we can mail out soon. The flyer should be a mix of great photos, some text, and a space for mailing and return address.

Target Market(s)

regular donors

Industry/Entity Type

Education

Font styles to use
Serif

Colors

Designer to choose colors to be used in the design.

Requirements
Must have
• Photos, text, a space on one side for a mailing label, a return address, and a stamp.
Nice to have
• attractive, eye-catching
Should not have
• boring

```html
<!DOCTYPE html>
<html lang="en">
<head>
<meta charset="utf-8">
<title>Riverside Community Family Center – Donor Postcard</title>
<link href="https://fonts.googleapis.com/css2?family=Questrial&family=Open+Sans:wght@400;600;700&display=swap" rel="stylesheet">
<style>
  :root{
    --teal:#5fa3b2;
    --teal-deep:#2f8ea0;
    --navy:#1d3a8f;
    --ink:#3d3d3d;
    --charcoal:#4a4a4a;
    --gold:#f2c21b;
    --gold-dark:#d9a50c;
    --paper:#ffffff;
    --mist:#eef1f3;
    --rule:#c9ced2;
    --stage:#e9e7e4;
  }
  *{box-sizing:border-box;margin:0;padding:0}
  html,body{width:1200px;height:1200px;overflow:hidden;background:var(--stage)}
  body{position:relative;font-family:"Open Sans",Arial,sans-serif;color:var(--ink)}
  .card{position:absolute;left:194px;width:812px;height:540px;overflow:hidden;background:var(--paper);box-shadow:0 4px 14px rgba(0,0,0,.18)}
  .card--front{top:24px}
  .card--back{top:636px}
  .card__art{position:absolute;inset:0;width:812px;height:540px}

  /* front */
  .brand-seal{position:absolute;left:79px;top:57px;width:152px;height:152px;border-radius:50%;display:flex;align-items:center;justify-content:center;text-align:center;flex-direction:column;gap:8px}
  .brand-seal__name{font-family:"Questrial",sans-serif;font-size:15px;line-height:1.25;color:var(--teal-deep);width:110px}
  .brand-seal__dot{width:12px;height:12px;border-radius:50%;background:var(--gold)}
  .headline{position:absolute;left:300px;top:74px;width:330px;text-align:center;font-family:"Questrial",sans-serif}
  .headline__lead{font-size:28px;letter-spacing:1px;color:var(--charcoal);line-height:1.15}
  .headline__teal{font-size:24px;color:var(--teal-deep);line-height:1.2;margin-top:2px}
  .headline__navy{font-size:24px;color:var(--navy);line-height:1.2}
  .ribbon{position:absolute;left:646px;top:52px;width:118px;text-align:center;font-family:"Open Sans",sans-serif;color:#2a2a2a;font-size:10px;line-height:19px}
  .ribbon__title{font-weight:700;font-size:10.5px}

  /* back */
  .appeal{position:absolute;left:25px;top:36px;width:330px;font-size:10px;line-height:13.6px;text-align:justify;color:#444}
  .contribute{position:absolute;left:22px;top:180px;width:330px}
  .contribute__title{font-family:"Open Sans",sans-serif;font-weight:700;font-size:16px;color:var(--teal-deep);display:flex;align-items:center;gap:8px}
  .contribute__title::after{content:"";flex:1;height:1px;background:var(--rule)}
  .contribute__text{font-family:"Questrial",sans-serif;font-size:16.5px;line-height:22px;color:#3a3a3a;margin-top:2px}
  .contribute__text svg{vertical-align:-3px;margin:0 4px}
  .footer{position:absolute;top:482px;font-size:10px;color:#fff;line-height:17px}
  .footer--org{left:24px}
  .footer--contact{left:254px}
  .footer__name{font-weight:700}
  .footer svg{vertical-align:-2px;margin-right:4px}
  .footer__indent{padding-left:18px}
  .mail-seal{position:absolute;left:420px;top:62px;width:84px;text-align:center;font-family:"Questrial",sans-serif;font-size:9.5px;line-height:1.25;color:var(--teal-deep)}
  .mail-seal__dot{width:9px;height:9px;border-radius:50%;background:var(--gold);margin:5px auto 0}
  .return-label{position:absolute;left:509px;top:60px;font-size:10.5px;color:#444}
</style>
</head>
<body>

<section class="card card--front">
  <svg class="card__art" viewBox="0 0 812 540" xmlns="http://www.w3.org/2000/svg">
    <defs>
      <clipPath id="front-panel">
        <path d="M70,200 C60,100 200,40 330,28 C480,15 560,40 646,44 C720,48 770,32 812,28 L812,524 L80,524 C40,440 50,300 70,200 Z"/>
      </clipPath>
      <linearGradient id="group-photo" x1="0" y1="0" x2="0" y2="1">
        <stop offset="0" stop-color="#ffffff" stop-opacity="1"/>
        <stop offset="0.12" stop-color="#cfd6d2"/>
        <stop offset="0.35" stop-color="#8c9c85"/>
        <stop offset="0.6" stop-color="#6d7e62"/>
        <stop offset="1" stop-color="#79a64c"/>
      </linearGradient>
      <linearGradient id="stage-photo" x1="0" y1="0" x2="0" y2="1">
        <stop offset="0" stop-color="#2a2a2e"/><stop offset="1" stop-color="#7a4a3c"/>
      </linearGradient>
      <linearGradient id="class-photo" x1="0" y1="0" x2="1" y2="1">
        <stop offset="0" stop-color="#b3a89a"/><stop offset="1" stop-color="#5d6f8a"/>
      </linearGradient>
    </defs>
    <rect width="812" height="540" fill="var(--teal)"/>
    <g clip-path="url(#front-panel)">
      <rect width="812" height="540" fill="#ffffff"/>
      <g role="img" aria-label="Group photo of children and staff seated on a park lawn in front of a playground and mountains">
        <rect x="0" y="150" width="812" height="380" fill="url(#group-photo)"/>
      </g>
    </g>
    <path d="M70,200 C60,100 200,40 330,28 C480,15 560,40 646,44 C720,48 770,32 812,28" fill="none" stroke="var(--charcoal)" stroke-width="6"/>
    <rect x="0" y="524" width="812" height="6" fill="#555"/>
    <circle cx="155" cy="133" r="82" fill="#e7ecee"/>
    <circle cx="155" cy="133" r="76" fill="#fff" stroke="var(--teal-deep)" stroke-width="1.5"/>
    <circle cx="74" cy="370" r="69" fill="#dfe8ea"/>
    <g role="img" aria-label="Photo of three girls in costume on stage"><circle cx="74" cy="370" r="63" fill="url(#stage-photo)" stroke="var(--teal-deep)" stroke-width="2"/></g>
    <circle cx="116" cy="466" r="59" fill="#dfe8ea"/>
    <g role="img" aria-label="Photo of children in a classroom"><circle cx="116" cy="466" r="53" fill="url(#class-photo)" stroke="var(--teal-deep)" stroke-width="2"/></g>
    <path d="M645,54 L651,46 L765,46 L771,54 L767,176 C740,184 712,196 708,206 C700,196 676,184 649,176 Z" fill="var(--gold-dark)" opacity=".6" transform="translate(2,3)"/>
    <path d="M645,54 L651,46 L765,46 L771,54 L767,176 C740,184 712,196 708,206 C700,196 676,184 649,176 Z" fill="var(--gold)"/>
  </svg>

  <div class="brand-seal">
    <span class="brand-seal__name">Riverside Community Family Center</span>
    <span class="brand-seal__dot"></span>
  </div>

  <div class="headline">
    <div class="headline__lead">EDUCATIONAL AND</div>
    <div class="headline__teal">community-building programs</div>
    <div class="headline__navy">for children, youth and families</div>
  </div>

  <div class="ribbon">
    <div class="ribbon__title">TO CONTRIBUTE</div>
    <div>Please Visit</div>
    <div><svg width="9" height="9" viewBox="0 0 10 10"><circle cx="5" cy="5" r="4.2" fill="none" stroke="#2a2a2a" stroke-width="1"/><path d="M1,5H9M5,1C3,3.5 3,6.5 5,9M5,1C7,3.5 7,6.5 5,9" fill="none" stroke="#2a2a2a" stroke-width=".8"/></svg> www.brightpathkids.org</div>
    <div>and click on the</div>
    <div>DONATE BUTTON</div>
  </div>
</section>

<section class="card card--back">
  <svg class="card__art" viewBox="0 0 812 540" xmlns="http://www.w3.org/2000/svg">
    <defs>
      <linearGradient id="music-photo" x1="0" y1="0" x2="1" y2="1">
        <stop offset="0" stop-color="#d8d2c6"/><stop offset="1" stop-color="#8a7a62"/>
      </linearGradient>
      <linearGradient id="lawn-photo" x1="0" y1="0" x2="0" y2="1">
        <stop offset="0" stop-color="#8fb6d8"/><stop offset=".45" stop-color="#6f8f6a"/><stop offset="1" stop-color="#5f9a3e"/>
      </linearGradient>
    </defs>
    <rect width="812" height="540" fill="#fff"/>
    <path d="M0,0 L394,0 C412,40 414,70 406,102 C385,210 350,340 326,446 L0,446 Z" fill="var(--mist)"/>
    <path d="M394,0 C412,40 414,70 406,102 C385,210 350,340 320,460" fill="none" stroke="var(--teal-deep)" stroke-width="7"/>
    <path d="M404,0 C420,40 422,72 414,104 C394,212 360,340 332,458" fill="none" stroke="var(--charcoal)" stroke-width="2"/>
    <path d="M0,430 C40,400 90,400 130,415 C170,430 160,448 200,432 C260,410 360,440 440,480 C500,510 550,530 586,540 L0,540 Z" fill="var(--teal)"/>
    <path d="M0,430 C40,400 90,400 130,415 C170,430 160,448 200,432 C260,410 360,440 440,480 C500,510 550,530 586,540" fill="none" stroke="var(--charcoal)" stroke-width="5"/>
    <circle cx="98" cy="317" r="76" fill="#fff"/>
    <g role="img" aria-label="Photo of children playing violin and trombone at music stands"><circle cx="98" cy="317" r="71" fill="url(#music-photo)" stroke="var(--teal-deep)" stroke-width="3"/></g>
    <circle cx="235" cy="320" r="76" fill="#fff"/>
    <g role="img" aria-label="Photo of children and a staff member sitting on the grass with a soccer ball"><circle cx="235" cy="320" r="71" fill="url(#lawn-photo)" stroke="var(--teal-deep)" stroke-width="3"/></g>
    <g stroke="var(--rule)" stroke-width="1">
      <line x1="509" y1="100" x2="678" y2="100"/>
      <line x1="509" y1="132" x2="678" y2="132"/>
      <line x1="509" y1="203" x2="771" y2="203"/>
      <line x1="509" y1="235" x2="771" y2="235"/>
      <line x1="509" y1="269" x2="771" y2="269"/>
      <line x1="509" y1="301" x2="771" y2="301"/>
    </g>
    <rect x="685.5" y="46.5" width="86" height="87" fill="none" stroke="#b8bec2" stroke-width="1"/>
  </svg>

  <p class="appeal">Riverside Community Family Center is in the middle of its 24th year of ministry and we need your help to finish our year strong! We need another $35,000 from our individual donors to help us meet our budget. We serve over 150 children each day at our four sites with a unique mix of homework help, a focus on literacy, enrichment classes - including music lessons, and a caring environment based on God’s love. Please help us continue to impact children and families through our high quality faith-based educational programs.</p>

  <div class="contribute">
    <div class="contribute__title">To contribute :</div>
    <div class="contribute__text">Please visit<svg width="16" height="16" viewBox="0 0 10 10"><circle cx="5" cy="5" r="4.2" fill="none" stroke="var(--teal-deep)" stroke-width=".9"/><path d="M1,5H9M5,1C3,3.5 3,6.5 5,9M5,1C7,3.5 7,6.5 5,9" fill="none" stroke="var(--teal-deep)" stroke-width=".7"/></svg>www.brightpathkids.org<br>and click on the donate button</div>
  </div>

  <div class="footer footer--org">
    <div class="footer__name"><svg width="12" height="11" viewBox="0 0 12 11"><path d="M6,0 L12,5 L10,5 L10,11 L7.5,11 L7.5,7.5 L4.5,7.5 L4.5,11 L2,11 L2,5 L0,5 Z" fill="#fff"/></svg>Riverside Community Family Center</div>
    <div class="footer__indent">218 N. Maple Ave., Fairview, CA 90010</div>
  </div>
  <div class="footer footer--contact">
    <div class="footer__name"><svg width="11" height="11" viewBox="0 0 12 12"><path d="M2.5,0.8 L4.5,0.8 L5.4,3.4 L4,4.6 C4.8,6.4 5.6,7.2 7.4,8 L8.6,6.6 L11.2,7.5 L11.2,9.5 C11.2,10.6 10.3,11.3 9.2,11.2 C4.8,10.6 1.4,7.2 0.8,2.8 C0.7,1.7 1.4,0.8 2.5,0.8 Z" fill="#fff"/></svg>(555) 014-2270</div>
    <div><svg width="11" height="11" viewBox="0 0 10 10"><circle cx="5" cy="5" r="4.2" fill="none" stroke="#fff" stroke-width=".9"/><path d="M1,5H9M5,1C3,3.5 3,6.5 5,9M5,1C7,3.5 7,6.5 5,9" fill="none" stroke="#fff" stroke-width=".7"/></svg><span style="font-size:11.5px">www.brightpathkids.org</span></div>
  </div>

  <div class="mail-seal">Riverside Community Family Center<div class="mail-seal__dot"></div></div>
  <div class="return-label">Return Address</div>
</section>

</body>
</html>
```